Medical Call Centre Needs a Web Design

We need a web design for a new company based in Melbourne called "Vantorra Services". We provide medical centres with administrative support by managing inbound calls to our clients facility. We require a clean, simple and easy to navigate website with an ultimate end product alike this - http://www.pelmarko.com/

The final design should communicate professionalism, new age and inovative.

Industry/Entity Type

It Company

```html
<!DOCTYPE html>
<html lang="en">
<head>
<meta charset="utf-8">
<title>Vantorra Services</title>
<link rel="stylesheet" href="https://fonts.googleapis.com/css2?family=Arvo:wght@700&family=Roboto:wght@400;500&display=swap">
<style>
:root{
  --yellow:#f0be2e;
  --yellow-soft:#f6d57e;
  --yellow-deep:#e2a91e;
  --red:#c4122f;
  --red-dark:#a80f27;
  --white:#ffffff;
}
*{margin:0;padding:0;box-sizing:border-box}
html,body{width:1200px;height:4206px;overflow:hidden}
body{position:relative;background:var(--yellow);font-family:"Roboto",Arial,sans-serif;color:var(--white)}
.abs{position:absolute}
.top-nav{left:0;top:0;width:1200px;height:50px;background:var(--red)}
.top-nav ul{list-style:none;position:absolute;left:144px;top:0;display:flex;height:50px}
.top-nav li{width:136px;text-align:center;line-height:50px;font-size:13px;font-weight:500;letter-spacing:.5px;border-right:1px solid var(--red-dark)}
.top-nav li:first-child{width:60px;text-align:left;color:var(--yellow)}
.search{left:812px;top:10px;width:230px;height:30px;background:var(--red-dark);display:flex}
.search span{flex:1;font-size:11px;line-height:30px;padding-left:10px;color:#e58a99}
.search i{width:36px;height:30px;background:var(--white);display:flex;align-items:center;justify-content:center}
.brand{left:137px;top:98px;width:135px;height:120px;background:var(--white);padding:14px 12px;font-family:"Arvo",Georgia,serif;font-weight:700;font-size:22px;line-height:28px;color:var(--red)}
.headline{left:137px;width:960px;font-family:"Arvo",Georgia,serif;font-weight:700;font-size:40px;line-height:56px;color:var(--red);white-space:nowrap}
.more{width:42px;height:42px}
.label{left:137px;font-size:27px}
.illustration{border-radius:8px}
.goals-title{left:137px;top:975px;font-size:30px;font-weight:400;color:var(--red)}
.goals{left:137px;top:1035px;list-style:none;font-size:18px}
.goals li{height:46px;line-height:46px}
.goals b{color:var(--red);font-weight:500;display:inline-block;width:34px}
.button{background:var(--red);text-align:center;font-size:24px;line-height:40px;height:40px;width:185px;left:875px}
.benefit{width:200px;text-align:center}
.ring{width:146px;height:146px;border-radius:50%;background:var(--yellow-soft);border:11px solid var(--white);display:flex;align-items:center;justify-content:center;margin:0 auto}
.benefit p{font-size:23px;margin-top:20px;white-space:nowrap}
.service{width:240px;text-align:center}
.service .ring{width:140px;height:140px}
.service p{font-size:23px;margin-top:10px;white-space:nowrap}
.footer{left:0;top:4010px;width:1200px;height:196px;background:var(--red);text-align:center}
.footer p{padding-top:50px;font-size:17px}
.social{display:flex;justify-content:center;gap:18px;margin-top:42px}
.social span{width:44px;height:44px;border-radius:50%;background:var(--white);display:block}
</style>
</head>
<body>

<nav class="top-nav abs">
  <ul><li>HOME</li><li>FEATURES</li><li>SERVICES</li><li>BENEFITS</li><li>ABOUT US</li></ul>
</nav>
<div class="search abs"><span>Enter Your Keywords</span><i><svg width="16" height="16" viewBox="0 0 16 16"><circle cx="6.5" cy="6.5" r="4.5" fill="none" stroke="#c4122f" stroke-width="2"/><path d="M10 10l4 4" stroke="#c4122f" stroke-width="2"/></svg></i></div>

<div class="brand abs">vantorra services</div>

<h1 class="headline abs" style="top:286px">Vantorra Services&nbsp; will provide a<br>support network to your administration<br>team will provide a support...</h1>
<svg class="more abs" style="left:1017px;top:482px" viewBox="0 0 42 42"><circle cx="21" cy="21" r="18" fill="var(--yellow-soft)" stroke="var(--yellow-deep)" stroke-width="2"/><path d="M13 17l8 8 8-8" fill="none" stroke="var(--yellow-deep)" stroke-width="3"/></svg>

<div class="label abs" style="top:572px">Hello</div>
<div class="illustration abs" role="img" aria-label="Illustration of call centre agents with headsets at laptops, linked by lines" style="left:137px;top:640px;width:880px;height:320px;background:linear-gradient(180deg,rgba(255,255,255,.18),rgba(255,255,255,.32))"></div>

<h2 class="goals-title abs">Our Goals</h2>
<ol class="goals abs">
  <li><b>1.</b>Simple and easy to do business with</li>
  <li><b>2.</b>Proactive and transparent with information, news and changes</li>
  <li><b>3.</b>Best-in-class and independently assesesed</li>
  <li><b>4.</b>Delivering a premium patient experience</li>
</ol>
<div class="button abs" style="top:1155px">Hello</div>

<h2 class="headline abs" style="top:1370px">Vantorra Services aim to<br>change the way medical facilities<br>interactwith patients...</h2>
<svg class="more abs" style="left:1017px;top:1560px" viewBox="0 0 42 42"><circle cx="21" cy="21" r="18" fill="var(--yellow-soft)" stroke="var(--yellow-deep)" stroke-width="2"/><path d="M13 17l8 8 8-8" fill="none" stroke="var(--yellow-deep)" stroke-width="3"/></svg>

<div class="label abs" style="top:1652px">Overview</div>
<div class="illustration abs" role="img" aria-label="Hand-drawn sketch of organization, culture and change initiative arrows" style="left:220px;top:1740px;width:640px;height:420px;background:linear-gradient(160deg,rgba(255,255,255,.14),rgba(196,18,47,.12))"></div>
<div class="button abs" style="top:2060px">Over view</div>

<h2 class="headline abs" style="top:2328px">Vantorra Services will allow you<br>to explore unmeasured communication<br>activities currently...</h2>
<svg class="more abs" style="left:1017px;top:2522px" viewBox="0 0 42 42"><circle cx="21" cy="21" r="18" fill="var(--yellow-soft)" stroke="var(--yellow-deep)" stroke-width="2"/><path d="M13 17l8 8 8-8" fill="none" stroke="var(--yellow-deep)" stroke-width="3"/></svg>

<div class="label abs" style="top:2615px">Benefits</div>

<div class="benefit abs" style="left:110px;top:2738px"><div class="ring"><svg width="60" height="60" viewBox="0 0 24 24"><path d="M6.6 10.8a15 15 0 006.6 6.6l2.2-2.2a1 1 0 011-.25 11.4 11.4 0 003.6.57 1 1 0 011 1V20a1 1 0 01-1 1A17 17 0 013 4a1 1 0 011-1h3.5a1 1 0 011 1c0 1.25.2 2.45.57 3.57a1 1 0 01-.25 1z" fill="none" stroke="var(--red)" stroke-width="1.4"/></svg></div><p>Volume</p></div>
<div class="benefit abs" style="left:298px;top:2738px"><div class="ring"><svg width="60" height="60" viewBox="0 0 24 24" fill="none" stroke="var(--red)" stroke-width="1.4"><rect x="3" y="7" width="13" height="14" rx="2"/><path d="M6 11h7M6 14h2M10 14h2M6 17h2M10 17h2"/><circle cx="17" cy="6" r="4"/><path d="M17 4v2h2"/></svg></div><p>Talk Time</p></div>
<div class="benefit abs" style="left:486px;top:2738px"><div class="ring"><svg width="60" height="60" viewBox="0 0 24 24" fill="none" stroke="var(--red)" stroke-width="1.4"><circle cx="10" cy="11" r="8"/><path d="M10 6v5h4"/><circle cx="17" cy="17" r="2"/><path d="M13.5 22a3.5 3.5 0 017 0"/></svg></div><p>Queue Time</p></div>
<div class="benefit abs" style="left:676px;top:2738px"><div class="ring"><svg width="60" height="60" viewBox="0 0 24 24" fill="none" stroke="var(--red)" stroke-width="1.4"><path d="M5.6 8.8a13 13 0 005.6 5.6l1.9-1.9a.9.9 0 01.9-.2 9.8 9.8 0 003 .5.9.9 0 01.9.9v3a.9.9 0 01-.9.9A14.6 14.6 0 012 3.2a.9.9 0 01.9-.9h3a.9.9 0 01.9.9c0 1 .2 2 .5 3a.9.9 0 01-.2.9z"/><circle cx="18" cy="17" r="4"/><path d="M16.5 15.5l3 3M19.5 15.5l-3 3"/></svg></div><p>Abandoned calls</p></div>
<div class="benefit abs" style="left:867px;top:2738px"><div class="ring"><svg width="60" height="60" viewBox="0 0 24 24" fill="none" stroke="var(--red)" stroke-width="1.4"><path d="M12 2l8 3v6c0 5-3.5 9-8 11-4.5-2-8-6-8-11V5z"/><path d="M8 12l3 3 5-6"/></svg></div><p>Quality Assurance</p></div>

<h2 class="headline abs" style="top:3114px">Vantorra services will manage<br>a diverted telecommunications<br>environment through...</h2>
<svg class="more abs" style="left:1017px;top:3308px" viewBox="0 0 42 42"><circle cx="21" cy="21" r="18" fill="var(--yellow-soft)" stroke="var(--yellow-deep)" stroke-width="2"/><path d="M13 17l8 8 8-8" fill="none" stroke="var(--yellow-deep)" stroke-width="3"/></svg>

<div class="label abs" style="top:3400px">Overview</div>
<div class="illustration abs" role="img" aria-label="White silhouette of a call centre operator wearing a headset" style="left:126px;top:3540px;width:290px;height:470px;border-radius:145px 145px 0 0;background:linear-gradient(180deg,rgba(255,255,255,.75),rgba(255,255,255,.95))"></div>

<div class="service abs" style="left:430px;top:3455px"><div class="ring"><svg width="54" height="54" viewBox="0 0 24 24" fill="none" stroke="var(--red)" stroke-width="1.4"><path d="M5.6 8.8a13 13 0 005.6 5.6l1.9-1.9a.9.9 0 01.9-.2 9.8 9.8 0 003 .5.9.9 0 01.9.9v3a.9.9 0 01-.9.9A14.6 14.6 0 012 3.2a.9.9 0 01.9-.9h3a.9.9 0 01.9.9c0 1 .2 2 .5 3a.9.9 0 01-.2.9z"/><circle cx="18" cy="17" r="3.5"/><path d="M18 15.5v3M16.5 17h3"/></svg></div><p>Providing Enquiries</p></div>
<div class="service abs" style="left:839px;top:3413px"><div class="ring"><svg width="54" height="54" viewBox="0 0 24 24" fill="none" stroke="var(--red)" stroke-width="1.4"><circle cx="10" cy="7" r="4"/><path d="M3 20a7 7 0 0110-6"/><circle cx="17" cy="17" r="3"/><path d="M19 19l2.5 2.5"/></svg></div><p>Account Enquiries</p></div>
<div class="service abs" style="left:637px;top:3617px"><div class="ring"><svg width="54" height="54" viewBox="0 0 24 24" fill="none" stroke="var(--red)" stroke-width="1.4"><rect x="3" y="5" width="18" height="16" rx="1"/><path d="M3 9h18M8 3v4M16 3v4"/><text x="12" y="18.5" font-size="7" font-family="Roboto,sans-serif" text-anchor="middle" fill="var(--red)" stroke="none">24</text></svg></div><p>Appointments</p></div>
<div class="service abs" style="left:867px;top:3757px"><div class="ring"><svg width="54" height="54" viewBox="0 0 24 24" fill="none" stroke="var(--red)" stroke-width="1.4"><path d="M5.6 8.8a13 13 0 005.6 5.6l1.9-1.9a.9.9 0 01.9-.2 9.8 9.8 0 003 .5.9.9 0 01.9.9v3a.9.9 0 01-.9.9A14.6 14.6 0 012 3.2a.9.9 0 01.9-.9h3a.9.9 0 01.9.9c0 1 .2 2 .5 3a.9.9 0 01-.2.9z"/><circle cx="18" cy="17" r="3.5"/><path d="M19.5 15.5l-3 3M16.5 16v2.5H19"/></svg></div><p>Internal</p></div>
<div class="service abs" style="left:494px;top:3800px"><div class="ring"><svg width="54" height="54" viewBox="0 0 24 24" fill="none" stroke="var(--red)" stroke-width="1.4"><path d="M5 3h10l4 4v14H5z"/><path d="M8 9h7M8 12h5M8 15h4"/><circle cx="17" cy="18" r="3"/><path d="M15.8 18l.9.9 1.6-1.7"/></svg></div><p>Results</p></div>

<footer class="footer abs">
  <p>Copyright 2014 Vantorra Services. All Rights Reserved</p>
  <div class="social">
    <span role="img" aria-label="Social network link"></span>
    <span role="img" aria-label="Social network link"></span>
    <span role="img" aria-label="Video channel link"></span>
    <span role="img" aria-label="Professional network link"></span>
  </div>
</footer>

</body>
</html>
```